Tolliver for Governor
We have chosen draft #108.
You have all done a great job and are amazing designers. I hope to work with you all again on future design projects for Tolliver For Governor.
Envelope: Move the address and URL up to just below the gold swoosh and you're missing a 't' in www.TolliverForGovernor.example On the back make the whole back white again add back in the emblem on the flap and make the It's Our Time fit across the back of the envelope in blue with a gradient.
Cards: Please see image and message.
Letterhead: Spot on!!!
We are now looking at #102, #103 and #106. Thank you to all the other designers, you've done a great job. There is still time for everyone to revise and resubmit their drafts, based on the comments we've made.
#90, Remove the email address from the letterhead and add Paid For By Tolliver For Governor on the same line as tolliverforgovernor.example, but on the far left side of page. Add address next to logo on front of envelope and lower It's Our Time on the back of the envelope. Remove the vertical It's Our Time from the two blue cards and center the logo on the blue card that should have no text.
#87, I like it. But everywhere you have tolliverforgovernor.example (except email addresses) remove it. I don't actually want the ""s around It's Our Time. It was away of telling you all what the exact text was. On the left side, the bottom two cards you could replace the URL with It's Our Time, just make the text bigger and bolder.
Envelope: I would like to see the back panel (not the flap) blue with white text saying "It's Our Time". On the front, move the address to the right side of the logo just under the gold swish. Add the URL under the address. Also, the address should be on 2 lines
P.O. Box 71832
Indianapolis, IN 46917
www.TolliverForGovernor.example
Card:
Logo-side, make the text much bigger (across the card bottom) and diffuse and spread out the white halo.
Info-side, move the phone number to it's own line above the address and move Name and title lines up to the lowest point in the gold swoosh. Try making the "tolliverforgovernor" in www.tolliverforgovernor.example blue like Jorel Drennick and capitalize the R,F and G.
Letterhead: on the same line as the phone and URL, but on the left side of the page, need "Paid For By Tolliver For Governor". Move the watermark logo up the page a little bit and add the line "It's Our Time" as light gray-ish watermark under it.
I done, please check
#80, please remove the URL from the logo-sides and insert the address on the info-side
please check private message
#45 and #43, let's lighten the background on the logo-side, remove the URL from both sides and insert the address.
#46, can we make the logo on the left side bigger, raise the name/title up more, insert the address and make the text bolder. On the logo side, lighter and more diffused. Also, please upload drafts for a letterhead and envelope.
I meant the logo-sides from #72 and #74
ALL: please include "Paid For By Tolliver For Governor" in small font at the bottom of the letterhead.
#70, this may be confusing, bare with me.
I like the info-side from #70 but; with the address added, name/title moved up and name in blue and remove the "phone" & "email" tags.
I like the logo-side but; make the white border around the logo the same size as the info-side and replace the URL with "It's Our Time" in font/style like "for Governor".
Would you be willing to add in the logo-side cards from both #71 and #74? Could you make the white border around the logos like the ones on the info-side in #70?
Also, need your drafts for an envelope and letterhead.
#13, I like the gradient on the front. Let's lighten the gradient, make the logo bigger and add some white diffusion around the logo (subtle). On the info side - like the flame in the lower corner. Raise the name and title area, make the name a little darker, remove the URL from the blue band, remove the "phone" and "email" tags, insert the full address. Maybe fill the center with a watermark of the logo? Also, would like to see some drafts for the letterhead and envelope.
Cards:
Info side- move name and title up more, put in the full address and add "It's Our Time" across the bottom in the same font style as "Tolliver".
Logo side- keep the logo transparency in the center of the logo, make the logo bigger and replace the white background with a light blue gradient (like in the images we uploaded).
Letterhead: remove all contact info except address, phone and URL. Add a "watermark" of all or part of the logo (w/ out the "Tolliver"). Also, at the bottom in the same line as the URL, but on the left side, add "Paid For By Tolliver For Governor".
Envelope: Insert the full address, move address and URL to the right of the logo (just under the gold line) on the back (not the flap) add "It's Our Time" feel free to try different colors in that area.
ALL: the card does not need to say "phone" or "email". You can use an icon if you want, but no need to spell it out. Also, only have the address, phone and URL on the letterhead.
Vandrel (#65,#64,#63,#62,#61,#60), What happened to the logo? Why is there sections (like a bar going across it) missing?
Sorry everyone, We've been on the road and unable to post more information or critiques.
Project Details:
1. This is a full stationary project (2-side business card, letterhead and envelope).
2. Front of business card should have either "It's Our Time" and the emblem from our provided logo or just the emblem. Background should be a light blue radial gradient with very light whitening behind emblem and/or text. Font for "It's Our Time" should match the fonts used for "Tolliver" in provided logo (colors either the same or white).
3. Address is:
PO Box 71832
4. Letterhead should have a watermark using all or part of the emblem from the provided logo.
5. Envelope should have a return address (PO Box from above).
6. Our campaign slogan is "It's Our Time".
7. On the business card there needs to be an area between the name/title area and the contact info.
8. Please do not fill in the transparent parts of the emblem or change it's color.
We will be picking a winner in the next 24 hours or less.
Good luck everyone :)

```html
<!DOCTYPE html>
<html lang="en">
<head>
<meta charset="utf-8">
<title>Tolliver for Governor – Business Cards</title>
<link href="https://fonts.googleapis.com/css2?family=Tinos:wght@400;700&display=swap" rel="stylesheet">
<style>
  :root {
    --stage: #2a2a2c;
    --card-white: #ffffff;
    --blue-deep: #0d4fa3;
    --blue-mid: #1f6fcb;
    --blue-light: #3a8fe0;
    --blue-ink: #1c4f9c;
    --mark-gold: #b89558;
    --text-gray: #555c66;
  }
  * { margin: 0; padding: 0; box-sizing: border-box; }
  html, body { width: 1200px; height: 1107px; overflow: hidden; background: var(--stage); }
  .board { position: relative; width: 1200px; height: 1107px; }
  .card {
    position: absolute; width: 490px; border-radius: 18px; overflow: hidden;
    box-shadow: 0 8px 24px rgba(0,0,0,.5);
  }
  .card--white { background: var(--card-white); }
  .card--blue { background: radial-gradient(ellipse at 60% 45%, var(--blue-light), var(--blue-mid) 55%, var(--blue-deep)); }
  .pos-a { left: 75px;  top: 66px;  height: 258px; }
  .pos-b { left: 618px; top: 66px;  height: 258px; }
  .pos-c { left: 75px;  top: 378px; height: 288px; }
  .pos-d { left: 618px; top: 378px; height: 288px; }
  .pos-e { left: 75px;  top: 696px; height: 288px; }
  .pos-f { left: 618px; top: 696px; height: 288px; }

  .band {
    position: absolute; left: 0; right: 0; top: 38px; height: 62px;
    background: linear-gradient(90deg, var(--blue-deep), var(--blue-light) 70%, #cfe2f6);
  }
  .mark-dot { position: absolute; border-radius: 50%; background: var(--mark-gold); }
  .halo { position: absolute; border-radius: 50%; background: radial-gradient(circle, rgba(255,255,255,.5), rgba(255,255,255,0) 70%); }
  .campaign-name {
    position: absolute; font-family: 'Tinos', 'Times New Roman', serif; font-weight: 700;
    color: var(--blue-ink); white-space: nowrap;
  }
  .campaign-name--white { color: #fff; }
  .person-name { position: absolute; left: 280px; top: 52px; font-family: 'Tinos', 'Times New Roman', serif; font-weight: 700; font-size: 20px; color: #fff; }
  .person-title { position: absolute; left: 280px; top: 78px; font-family: 'Tinos', serif; font-size: 10px; color: #e8f0fa; }
  .contact { position: absolute; left: 280px; top: 136px; font-family: 'Tinos', serif; font-size: 10px; color: var(--text-gray); line-height: 16px; list-style: none; }
  .contact li::before { content: ""; display: inline-block; width: 6px; height: 6px; margin-right: 6px; background: var(--blue-mid); border-radius: 1px; }
  .small-text { position: absolute; font-family: 'Tinos', serif; font-size: 10px; white-space: nowrap; }
  .vertical { writing-mode: vertical-rl; transform: rotate(180deg); }
  .tab { position: absolute; background: var(--blue-mid); }
</style>
</head>
<body>
<main class="board">

  <section class="card card--white pos-a" aria-label="Info side">
    <div class="band"></div>
    <div class="mark-dot" style="left:70px;top:60px;width:120px;height:120px" aria-hidden="true"></div>
    <div class="campaign-name" style="left:30px;top:200px;font-size:22px">Tolliver for Governor</div>
    <div class="person-name">Jorel Drennick</div>
    <div class="person-title">Campaign Manager</div>
    <ul class="contact">
      <li>(317) 555-0148</li>
      <li>jdrennick@tolliverforgovernor.example</li>
      <li>www.tolliverforgovernor.example</li>
    </ul>
  </section>

  <section class="card card--white pos-b" aria-label="Info side alternate">
    <div class="band"></div>
    <div class="mark-dot" style="left:70px;top:60px;width:120px;height:120px" aria-hidden="true"></div>
    <div class="campaign-name" style="left:30px;top:200px;font-size:22px">Tolliver for Governor</div>
    <div class="small-text" style="right:24px;top:146px;color:var(--text-gray)">jdrennick@tolliverforgovernor.example</div>
    <div class="tab" style="right:0;top:218px;width:10px;height:40px"></div>
  </section>

  <section class="card card--blue pos-c" aria-label="Logo side with large mark">
    <div class="halo" style="left:200px;top:0;width:300px;height:288px"></div>
    <div class="mark-dot" style="left:250px;top:30px;width:230px;height:230px;background:rgba(184,149,88,.85)" aria-hidden="true"></div>
    <div class="small-text" style="left:30px;top:138px;color:#dbe8f8">www.tolliverforgovernor.example</div>
  </section>

  <section class="card card--blue pos-d" aria-label="Logo side centered">
    <div class="halo" style="left:150px;top:5px;width:190px;height:190px"></div>
    <div class="mark-dot" style="left:180px;top:40px;width:130px;height:130px" aria-hidden="true"></div>
    <div class="campaign-name campaign-name--white" style="left:0;right:0;top:200px;text-align:center;font-size:26px">Tolliver for Governor</div>
    <div class="small-text vertical" style="right:26px;top:80px;color:#dbe8f8">www.tolliverforgovernor.example</div>
  </section>

  <section class="card card--white pos-e" aria-label="Vertical logo side">
    <div style="position:absolute;left:120px;top:0;right:0;bottom:0;background:linear-gradient(90deg,#fff,#f2f6fb)"></div>
    <div class="mark-dot" style="left:50px;top:66px;width:110px;height:110px" aria-hidden="true"></div>
    <div class="campaign-name vertical" style="left:180px;top:40px;font-size:22px">Tolliver for Governor</div>
    <div class="small-text vertical" style="right:78px;top:110px;color:var(--text-gray)">www.tolliverforgovernor.example</div>
    <div class="tab" style="right:0;bottom:0;width:70px;height:8px"></div>
  </section>

  <section class="card card--blue pos-f" aria-label="Logo side with base curve">
    <div class="halo" style="left:150px;top:5px;width:190px;height:190px"></div>
    <div class="mark-dot" style="left:180px;top:44px;width:130px;height:130px" aria-hidden="true"></div>
    <div class="campaign-name campaign-name--white" style="left:0;right:0;top:190px;text-align:center;font-size:26px">Tolliver for Governor</div>
    <svg style="position:absolute;left:0;bottom:0" width="490" height="60" viewBox="0 0 490 60" aria-hidden="true">
      <path d="M0 30 Q245 70 490 30 L490 60 L0 60 Z" fill="#1459b3"/>
    </svg>
  </section>

</main>
</body>
</html>
```